Sun Keel (www.sunkeel.com) web site development

Sun Keel is a new Fishing, Spearfishing Charter operator offering private charters in North Belize, Turneffe, Lighthouse Reef and the Blue Hole. The logo of the company has been designed by Pixelvane, some months ago. We have also developed a small brochure which can be the base for the website development (at least colors, fonts, etc.).
Pictures and Video should be an important asset of this website. We need to be able to update contents (video, photos), update prices and destinations, etc.

Target Market(s)

High hand, fishing and spearfishing enthusiasts.

Industry/Entity Type

Yacht charter

Coding

Coded - Design and coding required

Number of Pages Required

4 page

Colors
EB3D1F
EC4F4E
F09395
F8D3D4
FCEDEE

Requirements
Must have
• Optimized for phone and tablet navigation, must be easy to update with photos and video, connected to our Instagram and Facebook page,

```html
<!DOCTYPE html>
<html lang="en">
<head>
<meta charset="utf-8">
<title>Sun Keel – Fishing &amp; Spearfishing Charters</title>
<link href="https://fonts.googleapis.com/css2?family=Exo+2:ital,wght@1,700;1,800&family=Poppins:wght@400;500;600;700&display=swap" rel="stylesheet">
<style>
:root{
  --red:#e3242b;
  --red-soft:#ec4f4e;
  --navy:#22404f;
  --navy-deep:#1b3440;
  --ink:#333;
  --muted:#666;
  --line:#e6e6e6;
  --white:#fff;
}
*{box-sizing:border-box;margin:0;padding:0}
html,body{width:1200px;height:4688px;overflow:hidden}
body{position:relative;font-family:"Poppins",sans-serif;color:var(--ink);background:var(--white)}
.abs{position:absolute}
.display{font-family:"Exo 2",sans-serif;font-style:italic;font-weight:800;text-transform:uppercase;color:var(--navy);letter-spacing:-.5px}
.display em{color:var(--red);font-style:italic}
.btn{position:absolute;background:var(--red);color:#fff;font-size:12px;font-weight:700;text-transform:uppercase;display:flex;align-items:center;justify-content:center;letter-spacing:.3px}
.ph{position:absolute}

/* header */
.site-header{position:absolute;left:0;top:0;width:1200px;height:91px;background:#fff}
.brand{position:absolute;left:88px;top:28px;display:flex;align-items:center;gap:8px;font-weight:700;font-size:24px;color:var(--red)}
.brand i{width:14px;height:14px;border-radius:50%;background:var(--navy);display:block}
.nav{position:absolute;left:412px;top:38px;display:flex;gap:24px;font-size:12px;font-weight:500;color:#333}
.nav .active{color:var(--red)}
.lang{position:absolute;left:1044px;top:36px;display:flex;align-items:center;gap:6px;font-size:11px;color:#444}
.lang b{width:18px;height:18px;border-radius:50%;background:linear-gradient(#3b5fa8 50%,#d33 50%)}

/* hero */
.hero-title{left:86px;top:296px;font-size:68px;line-height:68px;color:#fff}

.section-title{text-align:center;left:0;width:1200px;font-size:40px;line-height:46px}
.card{position:absolute;background:#fff;box-shadow:0 6px 24px rgba(0,0,0,.09)}
.tag{position:absolute;left:22px;top:198px;background:var(--red);color:#fff;font-size:11px;font-weight:700;padding:4px 18px}
.card h3{position:absolute;left:20px;font-family:"Exo 2",sans-serif;font-style:italic;font-weight:800;font-size:14px;color:var(--navy);text-transform:uppercase}
.card p{position:absolute;left:20px;right:20px;font-size:12.5px;line-height:20px;color:var(--muted)}

.about-box{left:606px;top:1681px;width:503px;height:386px;background:#fff}
.feature{text-align:center}
.feature svg{position:absolute;left:50%;transform:translateX(-50%);top:36px}
.feature h4{position:absolute;left:0;right:0;top:130px;font-family:"Exo 2",sans-serif;font-style:italic;font-weight:700;font-size:17px;line-height:22px;color:var(--navy)}
.feature p{position:absolute;left:28px;right:28px;top:190px;font-size:12.5px;line-height:20px;color:var(--muted)}

.machine p,.machine li{font-size:13.5px;line-height:22px;color:#444;list-style:none}
.dot{position:absolute;width:12px;height:12px;border-radius:50%;background:var(--red)}

.meta{position:absolute;left:28px;top:253px;font-size:11px;color:#555}

.footer{left:0;top:4206px;width:1200px;height:482px;background:var(--navy)}
.footer h5{font-family:"Exo 2",sans-serif;font-style:italic;font-weight:700;font-size:16px;color:#fff;text-transform:uppercase}
.footer ul{list-style:none;margin-top:14px}
.footer li{font-size:13px;line-height:28px;color:#dfe6ea}
.social{position:absolute;width:32px;height:32px;border-radius:50%;border:2px solid #fff;top:4533px}
</style>
</head>
<body>

<header class="site-header">
  <div class="brand"><i></i>Sun Keel</div>
  <nav class="nav">
    <span class="active">HOME</span><span>CATEGORIES</span><span>ABOUT SUN KEEL</span><span>RENTAL &amp; ACCOMMODATION</span><span>BLOG</span><span>CONTACT US</span>
  </nav>
  <div class="lang"><b></b>ENG ▾</div>
</header>

<!-- hero -->
<div class="ph" style="left:0;top:91px;width:1200px;height:652px;background:linear-gradient(180deg,#8f99a3 0%,#5d6f80 40%,#1f3e5e 70%,#163352 100%)" role="img" aria-label="Angler fighting a bent rod on the bow of a boat at sea"></div>
<div class="ph" style="left:687px;top:743px;width:513px;height:80px;background:linear-gradient(180deg,#1a3a58,#c9d2da)" role="img" aria-label="Boat deck continuing below the hero"></div>
<h1 class="abs display hero-title">Fishing and<br>Spearfishing<br>Enthusiasts.</h1>
<div class="btn" style="left:88px;top:515px;width:152px;height:32px">Find out more</div>
<div class="ph" style="left:164px;top:620px;width:356px;height:356px;background:radial-gradient(circle at 50% 55%,#9a9a9a,#4a4a4a 55%,rgba(255,255,255,0) 72%)" role="img" aria-label="Spinning fishing reel with gold spool"></div>
<div class="abs" style="left:730px;top:720px;width:2px;height:230px;background:var(--red)"></div>
<div class="abs" style="left:708px;top:980px;transform:rotate(-90deg);transform-origin:left top;font-size:10px;letter-spacing:.5px;color:#333;white-space:nowrap">EXPLORE THE CHARGE</div>

<!-- charters -->
<h2 class="abs display section-title" style="top:1046px"><em>Just</em> bring your appetite<br>for adventure</h2>

<article class="card" style="left:164px;top:1175px;width:278px;height:364px">
  <div class="ph" style="left:0;top:0;width:278px;height:210px;background:linear-gradient(180deg,#9ec3e0,#6d8a6f)" role="img" aria-label="Two anglers holding a large catch"></div>
  <span class="tag">FROM US$1.000</span>
  <h3 style="top:244px">Fishing Private Charters</h3>
  <p style="top:274px">Our Fishing Charters are all Offshore Trips. Depending on your choice we can offer a...</p>
</article>
<article class="card" style="left:461px;top:1175px;width:278px;height:364px">
  <div class="ph" style="left:0;top:0;width:278px;height:210px;background:linear-gradient(180deg,#2aa0c8,#0d5f8a)" role="img" aria-label="Spearfisher underwater beside a large fish"></div>
  <span class="tag">FROM US$1.400</span>
  <h3 style="top:244px">Spearfishing Private Charters</h3>
  <p style="top:274px">We welcome all experience levels and you will be accompanied by a safe diver in the water...</p>
</article>
<article class="card" style="left:758px;top:1175px;width:278px;height:364px">
  <div class="ph" style="left:0;top:0;width:278px;height:210px;background:linear-gradient(135deg,#0a4f8c,#2fb5c9 55%,#0a5f9a)" role="img" aria-label="Aerial view of a reef and turquoise water"></div>
  <span class="tag">FROM US$1.200</span>
  <h3 style="top:244px">Snorkelling Private Charters</h3>
  <p style="top:274px">We offer snorkelling trips to the Hole Chan Marine Reserve, to Shark Ray Alley, Coral...</p>
</article>
<div class="ph" style="left:1030px;top:1285px;width:170px;height:245px;background:linear-gradient(135deg,rgba(60,60,60,.0) 40%,rgba(40,40,40,.35) 50%,rgba(60,60,60,0) 60%)" role="img" aria-label="Fishing rod and reel"></div>

<!-- about -->
<div class="ph" style="left:0;top:1566px;width:1200px;height:647px;background:linear-gradient(180deg,#ffffff 0%,#c9d3dc 20%,#5e7890 55%,#3d5a74 100%)" role="img" aria-label="White sport fishing boat cruising on open water"></div>
<section class="abs about-box">
  <h2 class="abs display" style="left:60px;top:60px;font-size:38px;white-space:nowrap"><em>About</em> Sun Keel</h2>
  <div class="abs" style="left:60px;top:108px;font-family:'Exo 2',sans-serif;font-style:italic;font-weight:700;font-size:11.5px;color:var(--navy)">WE WELCOME BOTH EXPERIENCED FISHERMEN/FREE DIVERS</div>
  <p class="abs" style="left:60px;top:158px;width:380px;font-size:13px;line-height:22px;color:#555">Sun Keel offers Fishing , Spearfishing and Snorkeling private charters in North Belize, Turneffe, Lighthouse Reef and the Blue Hole. No need to board crowded boats. Choose your privacy and let uspamper you with our exclusive service.</p>
  <div class="btn" style="left:60px;top:290px;width:124px;height:34px">Read more</div>
</section>

<!-- finest -->
<h2 class="abs display section-title" style="top:2302px"><em>The</em> finest fishing<br>experience</h2>
<div class="abs" style="left:578px;top:2398px;width:44px;height:1px;background:#ccc"></div>

<div class="card feature" style="left:91px;top:2440px;width:242px;height:297px">
  <svg width="80" height="80" viewBox="0 0 80 80" fill="none" stroke="#22404f" stroke-width="2"><path d="M20 70 Q10 30 40 10"/><path d="M40 10 L60 50"/><circle cx="26" cy="55" r="7"/><path d="M50 55 q8 -8 16 0 q-8 8 -16 0z"/></svg>
  <h4>Fishing<br>Destinations</h4>
  <p>Aenean sollicitudin lorem quis dis bibendum auctor nisi elit nec sem...</p>
</div>
<div class="card feature" style="left:350px;top:2440px;width:242px;height:297px">
  <svg width="90" height="80" viewBox="0 0 90 80" fill="none" stroke="#22404f" stroke-width="2"><path d="M45 8 V58"/><path d="M45 12 L25 55 H45"/><path d="M45 14 L68 55 H45"/><path d="M10 60 H80 L70 72 H20z"/><path d="M5 77 q10 -4 20 0 q10 4 20 0 q10 -4 20 0 q10 4 20 0"/></svg>
  <h4>Fishing<br>Charters</h4>
  <p>Aenean sollicitudin lorem quis dis bibendum auctor nisi elit nec sem...</p>
</div>
<div class="card feature" style="left:608px;top:2440px;width:242px;height:297px">
  <svg width="80" height="80" viewBox="0 0 80 80" fill="none" stroke="#22404f" stroke-width="2"><circle cx="40" cy="12" r="6"/><circle cx="22" cy="18" r="5"/><circle cx="58" cy="18" r="5"/><rect x="32" y="22" width="16" height="34" rx="3"/><rect x="15" y="27" width="14" height="30" rx="3"/><rect x="51" y="27" width="14" height="30" rx="3"/><path d="M36 56 V76 M44 56 V76 M19 57 V74 M25 57 V74 M55 57 V74 M61 57 V74"/></svg>
  <h4>Meet the<br>Crew</h4>
  <p>Aenean sollicitudin lorem quis dis bibendum auctor nisi elit nec sem...</p>
</div>
<div class="card feature" style="left:867px;top:2444px;width:242px;height:297px">
  <svg width="90" height="80" viewBox="0 0 90 80" fill="none" stroke="#22404f" stroke-width="2"><rect x="28" y="8" width="34" height="22" rx="2"/><path d="M12 40 L20 28 H70 L78 40 V62 H12z"/><circle cx="24" cy="50" r="5"/><circle cx="66" cy="50" r="5"/><path d="M36 48 H54 M36 54 H54"/><path d="M16 62 V72 H26 V62 M64 62 V72 H74 V62"/></svg>
  <h4>Meet the<br>Fleet</h4>
  <p>Aenean sollicitudin lorem quis dis bibendum auctor nisi elit nec sem...</p>
</div>
<div class="ph" style="left:0;top:2622px;width:215px;height:238px;background:radial-gradient(circle at 25% 50%,#5a4a20,#2b2b2b 45%,rgba(255,255,255,0) 70%)" role="img" aria-label="Gold and black fishing reel"></div>

<!-- fishing machine -->
<div class="abs display" style="left:226px;top:2900px;font-size:118px;line-height:110px;color:#ececec;letter-spacing:2px">DESTINATION</div>
<div class="ph" style="left:494px;top:2855px;width:706px;height:532px;background:linear-gradient(160deg,#5b9ad0 0%,#a9cde8 30%,#1e5f94 55%,#d9e4ea 100%)" role="img" aria-label="Trolling rods and gold reels mounted on the stern over the wake"></div>
<div class="abs" style="left:494px;top:3040px;width:142px;height:347px;background:#fff"></div>
<section class="abs machine" style="left:87px;top:3092px;width:420px">
  <h2 class="display" style="font-size:37px;line-height:46px;white-space:nowrap"><em>Our</em> fishing machine</h2>
  <p style="margin-top:20px">We outfit our boat with the latest electronics, up to date safety gear and finest equipment.</p>
  <ul style="margin-top:10px">
    <li>Kestrava 290 Open</li><li>LFT 31'10" ; Beam11'6"</li><li>Draft.: 2'0" ; Weight.10,000</li><li>Fuel: 302 gals.</li><li>Water 55 gals.</li><li>Engines: 2 x 350hp Inboard</li><li>Cruise Speed 20kn</li>
  </ul>
</section>
<div class="btn" style="left:87px;top:3393px;width:164px;height:34px">View accesories</div>
<span class="dot" style="left:998px;top:3330px"></span><span class="dot" style="left:1034px;top:3330px"></span>
<span class="dot" style="left:964px;top:3364px"></span><span class="dot" style="left:998px;top:3364px"></span><span class="dot" style="left:1034px;top:3364px"></span>
<span class="dot" style="left:964px;top:3436px"></span><span class="dot" style="left:998px;top:3436px"></span><span class="dot" style="left:1034px;top:3436px"></span>

<!-- blog -->
<h2 class="abs display section-title" style="top:3526px"><em>Latest</em> blog post</h2>

<article class="card" style="left:162px;top:3593px;width:281px;height:404px">
  <div class="ph" style="left:0;top:0;width:281px;height:219px;background:linear-gradient(180deg,#3fa6d8,#0e5d93)" role="img" aria-label="Snorkeler swimming among tropical fish"></div>
  <div class="meta">byJohn &nbsp;•&nbsp; January 2021</div>
  <h3 style="top:283px;left:28px;line-height:20px">Stay up to date with our<br>latest news.</h3>
  <p style="top:334px;left:28px;right:28px">Aenean sollicitudin bibendum is a auctor, nisi elit consequat...</p>
</article>
<article class="card" style="left:459px;top:3593px;width:281px;height:404px">
  <div class="ph" style="left:0;top:0;width:281px;height:219px;background:linear-gradient(180deg,#2c6fb0,#e6eef4)" role="img" aria-label="Angler reeling in a leaping marlin"></div>
  <div class="meta">byJohn &nbsp;•&nbsp; January 2021</div>
  <h3 style="top:283px;left:28px;line-height:20px">Stay up to date with our<br>latest news.</h3>
  <p style="top:334px;left:28px;right:28px">Aenean sollicitudin bibendum is a auctor, nisi elit consequat...</p>
</article>
<article class="card" style="left:756px;top:3593px;width:282px;height:404px">
  <div class="ph" style="left:0;top:0;width:282px;height:219px;background:linear-gradient(180deg,#7fa9cf,#2a5f86 60%,#c7c2a8)" role="img" aria-label="Angler holding a tuna on deck"></div>
  <div class="meta">byJohn &nbsp;•&nbsp; January 2021</div>
  <h3 style="top:283px;left:28px;line-height:20px">Stay up to date with our<br>latest news.</h3>
  <p style="top:334px;left:28px;right:28px">Aenean sollicitudin bibendum is a auctor, nisi elit consequat...</p>
</article>
<div class="ph" style="left:1040px;top:4000px;width:160px;height:128px;background:radial-gradient(circle at 40% 60%,#777,rgba(255,255,255,0) 55%)" role="img" aria-label="Spinning rod and reel"></div>

<!-- footer -->
<footer class="abs footer">
  <div class="abs" style="left:120px;top:120px;display:flex;align-items:center;gap:10px;font-size:40px;font-weight:700;color:#fff;white-space:nowrap"><i style="width:18px;height:18px;border-radius:50%;background:var(--red);display:block"></i>Sun Keel</div>
  <div class="abs" style="left:415px;top:156px"><h5>Quick links</h5><ul><li>Home</li><li>Categories</li><li>About Sun Keel</li><li>Rental &amp; accommodation</li><li>Blog</li><li>Contact Us</li></ul></div>
  <div class="abs" style="left:674px;top:156px"><h5>Information</h5><ul><li>Privacy Policy</li><li>Return Policy</li><li>Terms &amp; Condition</li><li>Contact us</li><li>FAQ's</li></ul></div>
  <div class="abs" style="left:872px;top:156px;width:250px"><h5>Contact us</h5>
    <div style="margin-top:22px;font-size:13px;line-height:20px;color:#dfe6ea;display:grid;grid-template-columns:20px 1fr;row-gap:14px">
      <svg width="12" height="10" viewBox="0 0 12 10"><rect width="12" height="10" rx="1" fill="#e3242b"/><path d="M0 1 L6 6 L12 1" stroke="#22404f" fill="none"/></svg><span>Email:<br>info@example.com</span>
      <svg width="12" height="12" viewBox="0 0 12 12"><path d="M2 1 L5 1 L6 4 L4 5 Q5 7 7 8 L8 6 L11 7 L11 10 Q5 11 1 4z" fill="#e3242b"/></svg><span>Phone:<br>+08 123-456-7890</span>
      <svg width="10" height="14" viewBox="0 0 10 14"><path d="M5 0 A5 5 0 0 1 10 5 Q10 8 5 14 Q0 8 0 5 A5 5 0 0 1 5 0z" fill="#e3242b"/><circle cx="5" cy="5" r="2" fill="#22404f"/></svg><span>Office Location:<br>Some address goes here with Northern Norway.</span>
    </div>
  </div>
  <div class="abs" style="left:0;top:428px;width:1200px;height:54px;background:var(--navy-deep);display:flex;align-items:center;justify-content:center;font-size:11px;font-weight:600;color:#fff">COPYRIGHT 2021 SUN KEEL ALL RIGHTS RESERVED.</div>
  <div class="abs" style="left:1130px;top:436px;width:38px;height:38px;border-radius:50%;background:var(--red);display:flex;align-items:center;justify-content:center"><svg width="12" height="12" viewBox="0 0 12 12"><path d="M6 11 V2 M2 6 L6 2 L10 6" stroke="#fff" stroke-width="1.6" fill="none"/></svg></div>
</footer>
<span class="social" style="left:141px"></span><span class="social" style="left:184px"></span><span class="social" style="left:226px"></span><span class="social" style="left:269px"></span>

<!-- mailing -->
<section class="abs" style="left:0;top:4128px;width:637px;height:146px;background:var(--red)">
  <h3 class="abs" style="left:84px;top:28px;font-family:'Exo 2',sans-serif;font-style:italic;font-weight:800;font-size:20px;color:#fff">JOIN OUR MAILING LIST</h3>
  <div class="abs" style="left:84px;top:66px;width:480px;height:46px;background:#fff;border:2px solid #fff;display:flex;align-items:center">
    <svg style="margin:0 10px 0 14px" width="14" height="11" viewBox="0 0 14 11"><rect width="14" height="11" rx="1" fill="#999"/><path d="M0 1 L7 6 L14 1" stroke="#fff" fill="none"/></svg>
    <span style="font-size:13px;color:#777;flex:1">Enter your email address</span>
    <span style="width:120px;height:42px;background:var(--navy);color:#fff;font-size:11px;font-weight:700;display:flex;align-items:center;justify-content:center">SUBSCRIBE</span>
  </div>
</section>

</body>
</html>
```